Business Card Design Project

We are an incubator company that helps young entrepreneur to launch new ideas into the market. We will be targeting investors or likewise; Angels, young entrepreneurs and technopreneurs.

Our logo is being tasked by artswarm to design, therefore there is no logo for now.
You can us Lanternfield Pte Ltd as the logo for the time being.

Please let us have some versions of modern and yet professional designs; for words, you can indicate e.g (address), (Title)

thanks

Target Market(s)

young entrepreneurs
angels, investors

Industry/Entity Type

Business

Colors
3176b5
ffffff

Requirements
Must have
• able to project out our name; Lanternfield
Should not have
• Nothing childish or cartoon

```html
<!DOCTYPE html>
<html lang="en">
<head>
<meta charset="utf-8">
<title>Lanternfield Business Card</title>
<link rel="stylesheet" href="https://fonts.googleapis.com/css2?family=Ubuntu:wght@400;500;700&display=swap">
<style>
  :root {
    --backdrop: #d9d8dc;
    --blue-bright: #2aa3de;
    --blue-deep: #1d64ad;
    --brand-blue: #3176b5;
    --ink: #1f5fa8;
    --paper-light: #ffffff;
    --paper-shade: #e9e9eb;
  }
  * { margin: 0; padding: 0; box-sizing: border-box; }
  html, body {
    width: 1200px;
    height: 900px;
    overflow: hidden;
    background: var(--backdrop);
    font-family: "Ubuntu", Arial, sans-serif;
  }
  .stage {
    position: relative;
    width: 1200px;
    height: 900px;
  }
  .card {
    position: absolute;
    top: 294px;
    width: 540px;
    height: 312px;
    background: var(--blue-bright);
    box-shadow: 0 6px 14px rgba(0, 0, 0, 0.28);
    overflow: hidden;
  }
  .card--front { left: 40px; }
  .card--back { left: 620px; }
  .card-band {
    position: absolute;
    left: 0;
    width: 100%;
    height: 10px;
    background: var(--blue-deep);
  }
  .card-band--top { top: 0; }
  .card-band--bottom { bottom: 0; }
  .card-panel {
    position: absolute;
    top: 28px;
    left: 28px;
    right: 28px;
    bottom: 28px;
    border-radius: 6px;
    background: linear-gradient(135deg, var(--paper-shade), var(--paper-light) 50%, var(--paper-shade));
  }
  .brand {
    position: absolute;
    left: 0;
    width: 100%;
    top: 118px;
    text-align: center;
    color: var(--brand-blue);
  }
  .brand-name {
    font-weight: 700;
    font-size: 44px;
    letter-spacing: 1px;
    line-height: 1;
  }
  .brand-tagline {
    margin-top: 8px;
    font-size: 10px;
    letter-spacing: 2.4px;
    color: var(--brand-blue);
  }
  .contact {
    position: absolute;
    left: 190px;
    top: 92px;
    color: var(--ink);
  }
  .contact-name {
    font-size: 27px;
    font-weight: 400;
    margin-bottom: 14px;
  }
  .contact-row {
    display: flex;
    align-items: center;
    height: 24px;
    font-size: 12px;
  }
  .contact-icon {
    width: 14px;
    height: 14px;
    margin-right: 12px;
    fill: var(--ink);
  }
</style>
</head>
<body>
<main class="stage">

  <section class="card card--front">
    <div class="card-band card-band--top"></div>
    <div class="card-band card-band--bottom"></div>
    <div class="card-panel"></div>
    <div class="brand">
      <div class="brand-name">LANTERNFIELD</div>
      <div class="brand-tagline">Guiding New Ventures Ahead</div>
    </div>
  </section>

  <section class="card card--back">
    <div class="card-band card-band--top"></div>
    <div class="card-band card-band--bottom"></div>
    <div class="card-panel"></div>
    <div class="contact">
      <div class="contact-name">Name Surname</div>
      <div class="contact-row">
        <svg class="contact-icon" viewBox="0 0 16 16" aria-hidden="true">
          <path d="M3 1l3 3-1.5 2c1 2 3 4 5 5L11.5 9.5l3 3L13 15C7 15 1 9 1 3z"/>
        </svg>
        <span>000 000 000</span>
      </div>
      <div class="contact-row">
        <svg class="contact-icon" viewBox="0 0 16 16" aria-hidden="true">
          <path d="M4 0h8a1 1 0 0 1 1 1v14a1 1 0 0 1-1 1H4a1 1 0 0 1-1-1V1a1 1 0 0 1 1-1zm1 2v10h6V2zm3 11a1 1 0 1 0 0 2 1 1 0 0 0 0-2z"/>
        </svg>
        <span>000 000 000</span>
      </div>
      <div class="contact-row">
        <svg class="contact-icon" viewBox="0 0 16 16" aria-hidden="true">
          <path d="M1 3h14v1L8 9 1 4zm0 2.5l7 5 7-5V13H1z"/>
        </svg>
        <span>email@website.com</span>
      </div>
      <div class="contact-row">
        <svg class="contact-icon" viewBox="0 0 16 16" aria-hidden="true">
          <path d="M8 1a7 7 0 1 0 0 14A7 7 0 0 0 8 1zm0 1.3c.8 0 1.7 1.5 2 3.7H6c.3-2.2 1.2-3.7 2-3.7zM5.9 7h4.2a12 12 0 0 1 0 2H5.9a12 12 0 0 1 0-2zM2.4 7h2.5a13 13 0 0 0 0 2H2.4a5.7 5.7 0 0 1 0-2zm8.7 0h2.5a5.7 5.7 0 0 1 0 2h-2.5a13 13 0 0 0 0-2zM6 10h4c-.3 2.2-1.2 3.7-2 3.7S6.3 12.2 6 10z"/>
        </svg>
        <span>www.website.com</span>
      </div>
    </div>
  </section>

</main>
</body>
</html>
```